Bag packaging design of sliced bread

The project is for design of line of sliced bread with different flavours. The brand of the bread will be "Valorina". The shape of the bread will be oval. The bread will be packed in a bag. I attach the layout of the bag. The bag will be closed with a plastic clip. I attach images of similar products. The idea is to have one main design and then each colour to be different type of bread like those in the images 2 and 5.

```html
<!DOCTYPE html>
<html lang="en">
<head>
<meta charset="utf-8">
<title>Valorina Sliced Bread – Bag Design</title>
<link rel="stylesheet" href="https://fonts.googleapis.com/css2?family=Oswald:wght@500;600&display=swap">
<style>
  :root {
    --bg-light: #e6e6ef;
    --bg-edge: #bcc1dd;
    --bag-film: rgba(255,255,255,0.35);
    --bag-edge: rgba(255,255,255,0.8);
    --bread-light: #e9c78f;
    --bread-mid: #d3a566;
    --bread-dark: #b98448;
    --band-red: #c51a2e;
    --band-red-light: #d92a3b;
    --gold: #c0874f;
    --badge-brown: #8a5a38;
    --cream: #fbf1dc;
    --wheat: #b98856;
  }
  * { margin: 0; padding: 0; box-sizing: border-box; }
  html, body { width: 1200px; height: 1048px; overflow: hidden; }
  body {
    background: radial-gradient(ellipse at 40% 45%, var(--bg-light) 0%, var(--bg-edge) 100%);
    font-family: "Oswald", "Arial Narrow", sans-serif;
    position: relative;
  }
  .bag {
    position: absolute;
    left: 447px; top: 110px;
    width: 340px; height: 868px;
  }
  .bag-neck {
    position: absolute;
    left: 50px; top: 0;
    width: 240px; height: 162px;
    background: var(--bag-film);
    border: 1px solid var(--bag-edge);
    border-radius: 10px 10px 0 0;
  }
  .bag-body {
    position: absolute;
    left: 0; top: 160px;
    width: 340px; height: 708px;
    border-radius: 60px;
    background: var(--bag-film);
    border: 1px solid var(--bag-edge);
    overflow: hidden;
  }
  .bread-photo {
    position: absolute;
    inset: 12px;
    border-radius: 52px;
    background: linear-gradient(90deg, var(--bread-dark) 0%, var(--bread-mid) 25%, var(--bread-light) 60%, var(--bread-mid) 100%);
  }
  .band {
    position: absolute;
    left: 96px; top: 0;
    width: 159px; height: 868px;
    background: linear-gradient(180deg, var(--band-red-light) 0%, var(--band-red) 100%);
    border-left: 2px solid var(--band-red);
    border-right: 2px solid var(--band-red);
  }
  .band::before, .band::after {
    content: "";
    position: absolute;
    top: 0; bottom: 0;
    width: 3px;
    background: var(--gold);
  }
  .band::before { left: 5px; }
  .band::after { right: 5px; }
  .wheat-field {
    position: absolute;
    left: 20px; bottom: 0;
    width: 300px; height: 126px;
    border-radius: 0 0 50px 50px;
    background: linear-gradient(180deg, rgba(185,136,86,0) 0%, rgba(185,136,86,0.7) 45%, var(--wheat) 100%);
  }
  .badge {
    position: absolute;
    left: 474px; top: 414px;
    width: 294px; height: 186px;
  }
  .badge svg { position: absolute; inset: 0; }
  .brand-name {
    position: absolute;
    left: 0; right: 0; top: 46px;
    text-align: center;
    font-size: 52px;
    font-weight: 600;
    color: var(--cream);
    letter-spacing: 1px;
  }
  .product-type {
    position: absolute;
    left: 0; right: 0; top: 120px;
    text-align: center;
    font-size: 17px;
    font-weight: 600;
    color: var(--badge-brown);
    letter-spacing: 1px;
  }
  .product-type span {
    background: var(--cream);
    padding: 1px 12px;
    border-radius: 3px;
  }
  .claim {
    position: absolute;
    left: 543px; top: 650px;
    width: 160px;
    text-align: center;
    color: var(--cream);
    font-size: 23px;
    font-weight: 500;
    line-height: 37px;
    text-transform: uppercase;
  }
  .net-weight {
    position: absolute;
    left: 543px; top: 913px;
    width: 160px;
    text-align: center;
    color: var(--cream);
    font-size: 19px;
    font-weight: 500;
  }
</style>
</head>
<body>
  <div class="bag">
    <div class="bag-neck"></div>
    <div class="bag-body">
      <div class="bread-photo" role="img" aria-label="Photograph of an oval sliced loaf seen through the clear bag"></div>
      <div class="wheat-field" role="img" aria-label="Illustration of wheat stalks along the bottom of the bag"></div>
    </div>
    <div class="band"></div>
  </div>

  <div class="badge">
    <svg width="294" height="186" viewBox="0 0 294 186">
      <ellipse cx="147" cy="93" rx="145" ry="91" fill="var(--cream)"/>
      <ellipse cx="147" cy="93" rx="137" ry="83" fill="var(--badge-brown)"/>
    </svg>
    <div class="brand-name">Valorina</div>
    <div class="product-type"><span>SLICED BREAD</span></div>
  </div>

  <p class="claim">Lorem ipsum<br>dolor sit amet,<br>consectetuer</p>
  <p class="net-weight">Net WT 500g</p>
</body>
</html>
```